【依頼の目的/概要】
電子書籍(bookrie)の表紙デザインをお願いします。

【画像サイズ】※BRPより抜粋
表紙ファイルの理想的な寸法は2,560×1,600ピクセルです。
注:画像の寸法は10,000×10,000ピクセルです。

【タイトル】
資格試験 ゴールダッシュ・速習・楽々学習術

サブタイトル
通れる学び方

【著者】
行政書士 社会保険労務士
森川澄江

【本の内容】
行政書士試験の勉強を短期間で仕上げて、合格する勉強法を
書いた本です。

【デザイン要望】
特にこだわりません。
素敵なデザインの応募を楽しみにしています。
※次点、次々点の方への参加報酬を設定しました。

その他
必要な情報がありましたらお問い合わせください。

本を以下に添付します。
本文中にエクセルで作成した表を挿入します。

明るく見やすく、わかり易い表現が良かったです。

皆様お疲れ様でした。
T_okabe様には訂正を速攻して頂きありがとうございました。
最後まで迷いました。
皆様のご依頼が増えますことをご祈念申し上げます。

```html
<!DOCTYPE html>
<html lang="ja">
<head>
<meta charset="utf-8">
<title>資格試験 ゴールダッシュ・速習・楽々学習術</title>
<link rel="stylesheet" href="https://fonts.googleapis.com/css2?family=Noto+Serif+JP:wght@700;900&family=Noto+Sans+JP:wght@700;900&display=swap">
<style>
  :root {
    --paper: #ffffff;
    --ink: #111111;
    --cover-red: #d52a2e;
    --accent-yellow: #ffe600;
    --illus-red: #e2494b;
    --illus-pale: #f6dada;
  }
  html, body {
    margin: 0;
    padding: 0;
    width: 750px;
    height: 1200px;
    overflow: hidden;
    background: var(--paper);
  }
  .cover {
    position: relative;
    width: 750px;
    height: 1200px;
    background: var(--paper);
    overflow: hidden;
  }
  .title-area .col {
    position: absolute;
    writing-mode: vertical-rl;
    font-family: "Noto Serif JP", serif;
    font-weight: 900;
    color: var(--ink);
    line-height: 1;
    white-space: nowrap;
  }
  .subtitle { left: 458px; top: 45px; font-size: 31px; letter-spacing: 1px; }
  .title-main { left: 392px; top: 98px; font-size: 56px; }
  .title-line { font-size: 48px; }
  .line-1 { left: 302px; top: 232px; }
  .line-2 { left: 228px; top: 232px; }
  .line-3 { left: 154px; top: 284px; }

  .illus-book {
    position: absolute;
    left: 95px; top: 68px;
    width: 185px; height: 135px;
  }
  .illus-pencil {
    position: absolute;
    left: 565px; top: 430px;
    width: 135px; height: 200px;
  }

  .band {
    position: absolute;
    left: 0; top: 645px;
    width: 750px; height: 555px;
    background: var(--cover-red);
    font-family: "Noto Sans JP", sans-serif;
    font-weight: 700;
  }
  .author-name {
    position: absolute;
    left: 218px; top: 52px;
    margin: 0;
    font-size: 40px;
    font-weight: 900;
    color: var(--paper);
    letter-spacing: 2px;
    white-space: pre;
  }
  .author-role {
    position: absolute;
    left: 218px; top: 110px;
    margin: 0;
    font-size: 22px;
    color: var(--paper);
    letter-spacing: 1px;
  }
  .band-rule {
    position: absolute;
    left: 40px; top: 186px;
    width: 670px; height: 2px;
    background: var(--paper);
  }
  .pitch {
    position: absolute;
    left: 0; top: 297px;
    width: 750px;
    margin: 0;
    padding: 0;
    list-style: none;
    color: var(--accent-yellow);
    font-size: 25px;
    font-weight: 900;
    line-height: 45px;
  }
  .pitch .lead { text-align: center; }
  .pitch .point { padding-left: 170px; font-size: 24px; }
  .pitch .close { padding-left: 150px; }
</style>
</head>
<body>
<main class="cover">
  <div class="illus-book" role="img" aria-label="開いた本のイラスト" style="background: linear-gradient(160deg, var(--illus-pale), var(--illus-red)); opacity: .55; border-radius: 6px;"></div>

  <header class="title-area">
    <p class="col subtitle" style="margin:0">通れる学び方</p>
    <h1 class="col title-main" style="margin:0">資格試験</h1>
    <p class="col title-line line-1" style="margin:0">・ゴールダッシュ</p>
    <p class="col title-line line-2" style="margin:0">・速習</p>
    <p class="col title-line line-3" style="margin:0">・楽々学習術</p>
  </header>

  <div class="illus-pencil" role="img" aria-label="赤い鉛筆のイラスト" style="background: linear-gradient(180deg, var(--illus-red), var(--cover-red)); opacity: .8; border-radius: 8px;"></div>

  <section class="band">
    <p class="author-name">森川　澄江</p>
    <p class="author-role">行政書士 社会保険労務士</p>
    <div class="band-rule"></div>
    <ul class="pitch">
      <li class="lead">４人の子育て中に合格できた著者が直接伝授！</li>
      <li class="point">・合格点の把握・受験の心構え</li>
      <li class="point">・願書提出日の確認・受験前の準備 etc</li>
      <li class="close">知れば思わず小躍りしてしまう情報が満載！</li>
    </ul>
  </section>
</main>
</body>
</html>
```